Banner Ad for Resume Writers

This ad is for www.kelbrancareers.com.au

The site offers a resume writing service in Australia. Take a look at the site for more info.

Colours to use: Blue, orange, yellow or whatever works.

Image specifications:
Pixel size: 160w X 600h (Skyscraper)
Image format: GIF (25K max)
Must have a border and must not use transparent backgrounds

Text can include:

'Professional Resume Writers'

and

'Is your resume good enough? Ask the Experts!'

The text 'Free resume health check' could be included but the banner should look good even if this text is not included as it may need to be removed.

Target Market(s)

Job seekers

Industry/Entity Type

Health

Nice to have
• It would be good to include an attractive smiling face making eye contact with the viewer.
Should not have
• Should not be too busy. Avoid clutter.

```html
<!DOCTYPE html>
<html lang="en">
<head>
<meta charset="utf-8">
<title>Kelbran Careers – Skyscraper Banner Set</title>
<link href="https://fonts.googleapis.com/css2?family=League+Gothic&family=Oswald:wght@300;400&display=swap" rel="stylesheet">
<style>
  :root {
    --stage: #ece7e1;
    --brand-red: #c8141c;
    --accent-yellow: #f6b400;
    --ink: #ffffff;
    --ink-dark: #141414;
    --ink-grey: #2d2d2d;
    --alert-red: #d51f23;
    --alert-orange: #ff6a13;
    --blue-light: #2c5590;
    --blue-dark: #132a52;
    --plum-light: #9a1266;
    --plum-dark: #4e0632;
    --rust-light: #9c3a0c;
    --rust-dark: #561804;
    --cta-light: #5aa5e0;
    --cta-dark: #1b5c9e;
    --photo-light: #f4f1ee;
    --photo-mid: #d9c6b4;
    --photo-skin: #e4b89c;
  }
  * { box-sizing: border-box; margin: 0; padding: 0; }
  html, body { width: 1200px; height: 715px; overflow: hidden; }
  body { background: var(--stage); position: relative; font-family: "Oswald", sans-serif; }

  .banner {
    position: absolute; top: 57px; width: 160px; height: 600px;
    border: 1px solid #1a1a1a; overflow: hidden;
    background: radial-gradient(ellipse at 50% 45%, var(--panel-light), var(--panel-dark) 85%);
    box-shadow: 0 2px 8px rgba(0,0,0,.35);
  }
  .banner--blue  { left: 70px;  --panel-light: var(--blue-light);  --panel-dark: var(--blue-dark); }
  .banner--photo-a { left: 245px; }
  .banner--photo-b { left: 420px; }
  .banner--photo-c { left: 595px; }
  .banner--plum  { left: 770px; --panel-light: var(--plum-light); --panel-dark: var(--plum-dark); }
  .banner--rust  { left: 945px; --panel-light: var(--rust-light); --panel-dark: var(--rust-dark); }
  .banner--photo { background: linear-gradient(180deg, #ffffff, var(--photo-light)); }

  .frame { position: absolute; inset: 0; width: 160px; height: 600px; }

  .portrait {
    position: absolute; left: 0; top: 352px; width: 160px; height: 248px;
    background: radial-gradient(ellipse 45% 55% at 50% 40%, var(--photo-skin), var(--photo-mid) 60%, var(--photo-light) 100%);
  }

  .brand {
    position: absolute; top: 6px; left: 0; width: 100%; text-align: center; color: var(--ink);
  }
  .brand__name {
    font-family: "League Gothic", sans-serif; font-weight: 400; color: var(--ink);
    display: block; line-height: 1; letter-spacing: 1px;
  }
  .brand__name--lead { font-size: 46px; }
  .brand__name--tail { font-size: 28px; margin-top: -3px; letter-spacing: 3px; }
  .brand__tagline {
    display: block; font-family: Arial, sans-serif; font-weight: 700; font-size: 8.5px; margin-top: 4px;
  }

  .pitch { position: absolute; left: 0; width: 100%; text-align: center; }
  .banner--solid .pitch { top: 166px; }
  .banner--photo .pitch { top: 137px; }

  .headline { font-family: "League Gothic", sans-serif; font-weight: 400; }
  .headline span { display: block; white-space: nowrap; }
  .headline__top { font-size: 35px; line-height: 1; }
  .headline__main { font-size: 66px; line-height: .86; }
  .headline__end { font-size: 57px; line-height: .88; }

  .banner--solid .headline__top, .banner--solid .headline__end { color: var(--ink); }
  .banner--solid .headline__main { color: var(--accent-yellow); }
  .banner--photo .headline__top { color: var(--top-color, var(--alert-red)); }
  .banner--photo .headline__main { color: var(--main-color, var(--ink-dark)); }
  .banner--photo .headline__end { color: var(--alert-red); }
  .banner--photo-b { --top-color: var(--alert-orange); --question-color: var(--alert-orange); }
  .banner--photo-c { --main-color: var(--ink-grey); }

  .rule { width: 138px; height: 1px; margin: 4px auto 0; }
  .banner--solid .rule { background: rgba(255,255,255,.8); }
  .banner--photo .rule { background: #555; }

  .question { line-height: 1.12; }
  .banner--solid .question { margin-top: 32px; }
  .banner--photo .question { margin-top: 4px; }
  .question span { display: block; white-space: nowrap; }
  .question__lead, .question__doubt { font-family: "Oswald", sans-serif; font-weight: 300; font-size: 18px; letter-spacing: -.6px; }
  .question__call { font-family: "League Gothic", sans-serif; font-size: 26px; line-height: 1; letter-spacing: .3px; }
  .banner--solid .question__lead { color: var(--accent-yellow); }
  .banner--solid .question__doubt, .banner--solid .question__call { color: var(--ink); }
  .banner--photo .question__lead { color: var(--ink-dark); }
  .banner--photo .question__doubt { color: var(--question-color, var(--alert-red)); }
  .banner--photo .question__call { color: var(--alert-red); }

  .cta {
    position: absolute; left: 11px; top: 548px; width: 140px; height: 36px; border-radius: 18px;
    background: linear-gradient(180deg, var(--cta-light), var(--cta-dark));
    border: 1px solid #0f3d6e; box-shadow: 0 1px 3px rgba(0,0,0,.5), inset 0 1px 0 rgba(255,255,255,.5);
    color: var(--ink); text-decoration: none; display: flex; align-items: center; justify-content: center; gap: 8px;
    font-family: "Oswald", sans-serif; font-weight: 300; font-size: 17px; letter-spacing: -.3px;
  }
  .cta__icon { width: 20px; height: 20px; }
</style>
</head>
<body>

<!-- Blue solid banner -->
<article class="banner banner--solid banner--blue">
  <svg class="frame" viewBox="0 0 160 600" aria-hidden="true">
    <path d="M0 0H160V128Q80 102 0 128Z" fill="var(--brand-red)"/>
    <path d="M0 128Q80 102 160 128V134Q80 108 0 134Z" fill="var(--accent-yellow)"/>
    <path d="M0 524Q80 500 160 524V600H0Z" fill="var(--accent-yellow)"/>
    <path d="M0 530Q80 506 160 530V600H0Z" fill="var(--brand-red)"/>
  </svg>
  <header class="brand">
    <span class="brand__name brand__name--lead">KELBRAN</span>
    <span class="brand__name brand__name--tail">CAREERS</span>
    <span class="brand__tagline">Let us write your success story</span>
  </header>
  <div class="pitch">
    <h2 class="headline"><span class="headline__top">PROFESSIONAL</span><span class="headline__main">RESUME</span><span class="headline__end">WRITERS</span></h2>
    <div class="rule"></div>
    <p class="question"><span class="question__lead">IS YOUR RESUME</span><span class="question__doubt">GOOD ENOUGH?</span><span class="question__call">ASK THE EXPERTS!</span></p>
  </div>
  <a class="cta" href="#">LEARN MORE <svg class="cta__icon" viewBox="0 0 20 20" aria-hidden="true"><circle cx="10" cy="10" r="9" fill="#fff"/><path d="M10 5V15M5 10H15" stroke="var(--cta-dark)" stroke-width="3"/></svg></a>
</article>

<!-- Photo banner A -->
<article class="banner banner--photo banner--photo-a">
  <div class="portrait" role="img" aria-label="Photo of a smiling young woman looking at the viewer"></div>
  <svg class="frame" viewBox="0 0 160 600" aria-hidden="true">
    <path d="M0 0H160V128Q80 102 0 128Z" fill="var(--brand-red)"/>
    <path d="M0 128Q80 102 160 128V134Q80 108 0 134Z" fill="var(--accent-yellow)"/>
  </svg>
  <header class="brand">
    <span class="brand__name brand__name--lead">KELBRAN</span>
    <span class="brand__name brand__name--tail">CAREERS</span>
    <span class="brand__tagline">Let us write your success story</span>
  </header>
  <div class="pitch">
    <h2 class="headline"><span class="headline__top">PROFESSIONAL</span><span class="headline__main">RESUME</span><span class="headline__end">WRITERS</span></h2>
    <div class="rule"></div>
    <p class="question"><span class="question__lead">IS YOUR RESUME</span><span class="question__doubt">GOOD ENOUGH?</span><span class="question__call">ASK THE EXPERTS!</span></p>
  </div>
  <a class="cta" href="#">LEARN MORE <svg class="cta__icon" viewBox="0 0 20 20" aria-hidden="true"><circle cx="10" cy="10" r="9" fill="#fff"/><path d="M10 5V15M5 10H15" stroke="var(--cta-dark)" stroke-width="3"/></svg></a>
</article>

<!-- Photo banner B -->
<article class="banner banner--photo banner--photo-b">
  <div class="portrait" role="img" aria-label="Photo of a smiling young woman looking at the viewer"></div>
  <svg class="frame" viewBox="0 0 160 600" aria-hidden="true">
    <path d="M0 0H160V128Q80 102 0 128Z" fill="var(--brand-red)"/>
    <path d="M0 128Q80 102 160 128V134Q80 108 0 134Z" fill="var(--accent-yellow)"/>
  </svg>
  <header class="brand">
    <span class="brand__name brand__name--lead">KELBRAN</span>
    <span class="brand__name brand__name--tail">CAREERS</span>
    <span class="brand__tagline">Let us write your success story</span>
  </header>
  <div class="pitch">
    <h2 class="headline"><span class="headline__top">PROFESSIONAL</span><span class="headline__main">RESUME</span><span class="headline__end">WRITERS</span></h2>
    <div class="rule"></div>
    <p class="question"><span class="question__lead">IS YOUR RESUME</span><span class="question__doubt">GOOD ENOUGH?</span><span class="question__call">ASK THE EXPERTS!</span></p>
  </div>
  <a class="cta" href="#">LEARN MORE <svg class="cta__icon" viewBox="0 0 20 20" aria-hidden="true"><circle cx="10" cy="10" r="9" fill="#fff"/><path d="M10 5V15M5 10H15" stroke="var(--cta-dark)" stroke-width="3"/></svg></a>
</article>

<!-- Photo banner C -->
<article class="banner banner--photo banner--photo-c">
  <div class="portrait" role="img" aria-label="Photo of a smiling young woman looking at the viewer"></div>
  <svg class="frame" viewBox="0 0 160 600" aria-hidden="true">
    <path d="M0 0H160V128Q80 102 0 128Z" fill="var(--brand-red)"/>
    <path d="M0 128Q80 102 160 128V134Q80 108 0 134Z" fill="var(--accent-yellow)"/>
  </svg>
  <header class="brand">
    <span class="brand__name brand__name--lead">KELBRAN</span>
    <span class="brand__name brand__name--tail">CAREERS</span>
    <span class="brand__tagline">Let us write your success story</span>
  </header>
  <div class="pitch">
    <h2 class="headline"><span class="headline__top">PROFESSIONAL</span><span class="headline__main">RESUME</span><span class="headline__end">WRITERS</span></h2>
    <div class="rule"></div>
    <p class="question"><span class="question__lead">IS YOUR RESUME</span><span class="question__doubt">GOOD ENOUGH?</span><span class="question__call">ASK THE EXPERTS!</span></p>
  </div>
  <a class="cta" href="#">LEARN MORE <svg class="cta__icon" viewBox="0 0 20 20" aria-hidden="true"><circle cx="10" cy="10" r="9" fill="#fff"/><path d="M10 5V15M5 10H15" stroke="var(--cta-dark)" stroke-width="3"/></svg></a>
</article>

<!-- Plum solid banner -->
<article class="banner banner--solid banner--plum">
  <svg class="frame" viewBox="0 0 160 600" aria-hidden="true">
    <path d="M0 0H160V128Q80 102 0 128Z" fill="var(--brand-red)"/>
    <path d="M0 128Q80 102 160 128V134Q80 108 0 134Z" fill="var(--accent-yellow)"/>
    <path d="M0 524Q80 500 160 524V600H0Z" fill="var(--accent-yellow)"/>
    <path d="M0 530Q80 506 160 530V600H0Z" fill="var(--brand-red)"/>
  </svg>
  <header class="brand">
    <span class="brand__name brand__name--lead">KELBRAN</span>
    <span class="brand__name brand__name--tail">CAREERS</span>
    <span class="brand__tagline">Let us write your success story</span>
  </header>
  <div class="pitch">
    <h2 class="headline"><span class="headline__top">PROFESSIONAL</span><span class="headline__main">RESUME</span><span class="headline__end">WRITERS</span></h2>
    <div class="rule"></div>
    <p class="question"><span class="question__lead">IS YOUR RESUME</span><span class="question__doubt">GOOD ENOUGH?</span><span class="question__call">ASK THE EXPERTS!</span></p>
  </div>
  <a class="cta" href="#">LEARN MORE <svg class="cta__icon" viewBox="0 0 20 20" aria-hidden="true"><circle cx="10" cy="10" r="9" fill="#fff"/><path d="M10 5V15M5 10H15" stroke="var(--cta-dark)" stroke-width="3"/></svg></a>
</article>

<!-- Rust solid banner -->
<article class="banner banner--solid banner--rust">
  <svg class="frame" viewBox="0 0 160 600" aria-hidden="true">
    <path d="M0 0H160V128Q80 102 0 128Z" fill="var(--brand-red)"/>
    <path d="M0 128Q80 102 160 128V134Q80 108 0 134Z" fill="var(--accent-yellow)"/>
    <path d="M0 524Q80 500 160 524V600H0Z" fill="var(--accent-yellow)"/>
    <path d="M0 530Q80 506 160 530V600H0Z" fill="var(--brand-red)"/>
  </svg>
  <header class="brand">
    <span class="brand__name brand__name--lead">KELBRAN</span>
    <span class="brand__name brand__name--tail">CAREERS</span>
    <span class="brand__tagline">Let us write your success story</span>
  </header>
  <div class="pitch">
    <h2 class="headline"><span class="headline__top">PROFESSIONAL</span><span class="headline__main">RESUME</span><span class="headline__end">WRITERS</span></h2>
    <div class="rule"></div>
    <p class="question"><span class="question__lead">IS YOUR RESUME</span><span class="question__doubt">GOOD ENOUGH?</span><span class="question__call">ASK THE EXPERTS!</span></p>
  </div>
  <a class="cta" href="#">LEARN MORE <svg class="cta__icon" viewBox="0 0 20 20" aria-hidden="true"><circle cx="10" cy="10" r="9" fill="#fff"/><path d="M10 5V15M5 10H15" stroke="var(--cta-dark)" stroke-width="3"/></svg></a>
</article>

</body>
</html>
```